Photographer website

This website will contain information to sell the services of marvello tebani an up and coming photographer based in london

Target Market(s)

SME's for corporate head shots
mums for kids parties
actors - for headshots
up and coming models

Industry/Entity Type

Photographer

Number of Pages Required

3 page

Requirements
Must have
• Home
• About me
• Contact me
• Portfolio or gallery

```html
<!DOCTYPE html>
<html lang="en">
<head>
<meta charset="utf-8">
<title>Marvello Tebani — Photographer</title>
<link rel="stylesheet" href="https://fonts.googleapis.com/css2?family=Montserrat:wght@400;500;600;700&family=Dancing+Script:wght@400;600&display=swap">
<style>
:root{
  --accent:#f39c12;
  --dark:#2b2a28;
  --darker:#1e1d1c;
  --panel:#161616;
  --ink:#2a2a2a;
  --muted:#555;
  --light:#efefef;
  --white:#fff;
}
*{margin:0;padding:0;box-sizing:border-box}
html,body{width:748px;height:1200px;overflow:hidden}
body{position:relative;font-family:"Montserrat",sans-serif;color:var(--ink);background:var(--white)}
.abs{position:absolute}
.accent{color:var(--accent)}

/* hero */
.hero{position:absolute;left:0;top:0;width:748px;height:349px;overflow:hidden}
.hero-photo{position:absolute;inset:0;background:linear-gradient(115deg,#3a3632 0%,#5a5048 35%,#8a7f78 62%,#b6a9a2 80%,#6e6660 100%)}
.hero-shade{position:absolute;inset:0;background:linear-gradient(90deg,rgba(0,0,0,.35),rgba(0,0,0,.05) 60%,rgba(0,0,0,.25))}
.side-nav{position:absolute;left:97px;top:30px;width:127px;height:209px;background:rgba(14,14,14,.92);padding:0 17px}
.brand{position:absolute;left:17px;top:40px;width:95px;color:var(--white);font-weight:500;font-size:13px;letter-spacing:.5px;line-height:1.2}
.brand small{display:block;font-size:7px;letter-spacing:4px;margin-top:3px;text-align:right}
.side-nav ul{list-style:none;position:absolute;left:17px;top:83px;width:93px}
.side-nav li{font-size:7.5px;letter-spacing:1px;color:var(--white);height:22px;line-height:22px}
.side-nav li.active{color:var(--accent);border-bottom:1px solid #444}
.social{position:absolute;left:17px;top:179px;display:flex;gap:11px}
.social span{width:7px;height:7px;border-radius:50%;background:#bbb}
.social span.on{background:var(--accent)}
.hero-frame{position:absolute;left:567px;top:155px;width:83px;height:173px;border:2px solid var(--accent)}
.hero-title{position:absolute;right:112px;top:168px;text-align:right;color:var(--white);font-weight:600;font-size:29px;line-height:33px;letter-spacing:-.3px}
.hero-text{position:absolute;right:112px;top:276px;width:250px;text-align:right;color:var(--white);font-size:8px;line-height:11px}

/* about */
.about{position:absolute;left:0;top:349px;width:748px;height:279px;background:var(--white)}
.about-photo{position:absolute;left:97px;top:40px;width:175px;height:199px;background:linear-gradient(160deg,#3b3550,#7a7690 55%,#d9d8e2)}
.section-title{font-size:15px;font-weight:400;letter-spacing:.6px;color:var(--ink)}
.section-title b{font-weight:500;color:var(--accent)}
.about-title{position:absolute;left:334px;top:38px}
.rule{position:absolute;height:1px;background:#cfcfcf}
.about-lead{position:absolute;left:334px;top:71px;width:260px;font-size:8.5px;font-weight:600;line-height:11px}
.about-lead span{font-weight:500}
.about-body{position:absolute;left:334px;top:104px;width:300px;font-size:7.5px;line-height:11px;color:var(--muted)}
.about-body p+p{margin-top:11px}
.btn-outline{position:absolute;height:20px;border:1px solid #999;border-left:4px solid var(--accent);font-size:7px;line-height:18px;text-align:center;color:var(--ink)}
.btn-outline::after{content:" »"}

/* gallery */
.gallery{position:absolute;left:0;top:628px;width:748px;height:415px;background:linear-gradient(180deg,var(--dark),#23221f)}
.gallery-title{position:absolute;left:0;width:748px;top:37px;text-align:center;color:var(--white)}
.tile{position:absolute}
.tile.a{left:97px;top:76px;width:132px;height:127px;background:linear-gradient(160deg,#cfcfcf,#7a7a7a)}
.tile.b{left:97px;top:208px;width:132px;height:127px;background:linear-gradient(160deg,#3d3d3d,#9a9a9a)}
.tile.c{left:234px;top:76px;width:232px;height:259px;background:linear-gradient(170deg,#2f3330,#6e6a62 55%,#4a4a48)}
.tile.d{left:471px;top:76px;width:180px;height:127px;background:linear-gradient(160deg,#e4e4e4,#8c8c8c)}
.tile.e{left:471px;top:208px;width:180px;height:127px;background:linear-gradient(160deg,#111,#6a6a6a)}
.caption{position:absolute;left:234px;top:285px;width:232px;height:50px;background:var(--accent);color:var(--white);font-size:7.5px;font-weight:500;line-height:10px;padding:15px 0 0 15px}
.cap-icon{position:absolute;top:13px;width:25px;height:25px;border-radius:50%;background:var(--white)}
.btn-dark{border-color:#bbb;color:var(--white)}

/* quote */
.quote{position:absolute;left:0;top:1043px;width:748px;height:124px;background:var(--light);text-align:center}
.quote h2{position:absolute;left:0;width:748px;top:16px;font-family:"Dancing Script",cursive;font-weight:400;font-size:21px;color:#333}
.quote h3{position:absolute;left:0;width:748px;top:44px;font-family:"Dancing Script",cursive;font-weight:400;font-size:15px;color:#333}
.quote .accent{font-weight:600}
.btn-solid{position:absolute;left:334px;top:80px;width:80px;height:20px;background:var(--accent);color:var(--white);font-size:7px;line-height:20px}
.btn-solid::after{content:" »"}

/* footer */
.footer{position:absolute;left:0;top:1167px;width:748px;height:33px;background:var(--darker);color:var(--white)}
.copy{position:absolute;left:97px;top:12px;font-size:7px}
.foot-nav{position:absolute;right:97px;top:6px;display:flex;gap:11px;font-size:7px;list-style:none}
.foot-nav li.active{color:var(--accent)}
.foot-social{position:absolute;right:97px;top:21px;display:flex;gap:10px}
.foot-social span{width:5px;height:5px;border-radius:50%;background:#aaa}
.foot-social span.on{background:var(--accent)}
</style>
</head>
<body>

<header class="hero">
  <div class="hero-photo" role="img" aria-label="Photographer holding a camera over a city street"></div>
  <div class="hero-shade"></div>
  <nav class="side-nav">
    <div class="brand">Marvello<small>STUDIO</small></div>
    <ul>
      <li class="active">→ Home</li>
      <li>About me</li>
      <li>My Portfolio</li>
      <li>Contact me</li>
    </ul>
    <div class="social"><span></span><span class="on"></span><span></span><span></span><span></span></div>
  </nav>
  <div class="hero-frame"></div>
  <h1 class="hero-title">HI<br>I'M TOPPIC<br>PHOTOGRAPHER</h1>
  <p class="hero-text">I specialise in portraiture photography. My first few years behind the camera is when I fell in love with this particular type of photography.</p>
</header>

<section class="about">
  <div class="about-photo" role="img" aria-label="Portrait of the photographer in a white t-shirt"></div>
  <h2 class="section-title about-title">About <b>Me</b></h2>
  <div class="rule" style="left:422px;top:46px;width:95px"></div>
  <p class="about-lead">Hi My name is <span class="accent">Marvello Tebani</span> Born in East Brazil, grew up in Spain.</p>
  <div class="about-body">
    <p>I now live in London but I travel internationally for work.<br>When traveling around the globe I'm always looking for the perfect setting to create that special Picture. My goal is to show that little part that can't be appreciated on the naked eye alone.</p>
    <p>I'm incredibly well traveled sometimes shy in the crowds but very curious and enthusiastic of people and their imagery.</p>
  </div>
  <div class="btn-outline" style="left:334px;top:193px;width:80px">Explore More</div>
</section>

<section class="gallery">
  <h2 class="section-title gallery-title" style="color:#fff">My Awsome <b>Gallery</b></h2>
  <div class="rule" style="left:192px;top:47px;width:95px;background:#555"></div>
  <div class="rule" style="left:461px;top:47px;width:95px;background:#555"></div>
  <div class="tile a" role="img" aria-label="Black and white portrait of a man"></div>
  <div class="tile b" role="img" aria-label="Black and white portrait of a man in a white t-shirt"></div>
  <div class="tile c" role="img" aria-label="Featured portrait of a blond man"></div>
  <div class="tile d" role="img" aria-label="Black and white close portrait of a man"></div>
  <div class="tile e" role="img" aria-label="Dark low-key portrait of a man"></div>
  <div class="caption">Lorium Photograph Dummy<br>name
    <span class="cap-icon" style="left:162px"></span>
    <span class="cap-icon" style="left:197px"></span>
  </div>
  <div class="btn-outline btn-dark" style="left:334px;top:355px;width:80px">View All</div>
</section>

<section class="quote">
  <h2>I don't take Photographs, I Make it <span class="accent">live...</span></h2>
  <h3>Let us <span class="accent">Freeze</span> your Expressions forever...</h3>
  <div class="btn-solid">Contact Me</div>
</section>

<footer class="footer">
  <p class="copy">© 2016 <span class="accent">Marvello Tebani</span>. All Rights Reserved.</p>
  <ul class="foot-nav">
    <li class="active">Home</li><li>About me</li><li>My Portfolio</li><li>Contact me</li>
  </ul>
  <div class="foot-social"><span></span><span class="on"></span><span></span><span></span><span></span></div>
</footer>

</body>
</html>
```